Modern Small Law Firm Website To Look Cutting Edge

I need a website design for a new, single-attorney law firm. The firm will be called "The Thornwell Law Group." Our goal is to handle car accident and general personal injury lawsuits for individuals.

Our selling points are: (1) We charge less so you keep more; (2) We have experience and success trying and settling multi-million dollar cases; (3) We use modern technology to make the whole process simple, easy and hassle-free for clients.

Also because we are a one-man law firm, the clients will personally know the lawyer and have access to them. For that reason, I thought a good big tagline for the website would be "KNOW YOUR LAWYER"

I like the idea of splitting the website vertically down the middle, with the left side having a blue background, a picture of me, and big white lettering for the tagline, and the right side having a white background with blue lettering and headlines. I don't want navy blue or royal blue, but a more bright and eye-catching blue color. We can experiment with different shades.

I would be curious about how it could look with some minor orange accent coloring somewhere.

I need to feature prominently, probably in the top left corner, this phone number: 504-917-2083.

This will be used as much by mobile users as it would be by desktop/computer users.

The final design should communicate trust, convenience and cutting edge technology that leads to success.

Finally, I would be curious how we can have a sleek looking info submission box somewhere on the right side nearer the bottom that features different combinations of presenting these phrases: "QUICK QUESTION? QUICK ANSWER" The info submission button could say "Ask"

I am uploading two different pictures of me that can be used. The gray backgrounds are not necessary or good, if there is a way to cut them out that would be great. I can try and get that if needed.

Target Market(s)

Individuals who have been hurt by others, mostly in car accidents. They will be frustrated, inconvenienced and need to be soothed.

Industry/Entity Type

Legal

Number of Pages Required

1 page

Font styles to use
Sans Serif

Colors
0692cd
33a6d7
85cae6
faa54b
f78f20
3276b5

Requirements
Must have
• If you have started designing already, please note that the project description information is more important than the image that I uploaded originally. It has since been deleted.
• Also please now use the color photo that has been uploaded.
Nice to have
• I really want a clean and simple website design with not a lot of clutter. I'd like to avoid the typical law firm websites that you see that have tool bars across the top and basic borders/columns everywhere. It needs to grab your attention and look a little more cutting edge and different.
• Let's experiment with different eye-catching ways to present the three value propositions I noted.
• Also if the screen is split vertically with the left and right side being blue and white, maybe we can experiment with different ways that the two colors could fade into each other as opposed to just a line where one color starts and the other ends.
• And maybe the blue/white backgrounds could be textured somehow so that they don't appear flat. Perhaps we could try using differing shades of blue to give the appearance of pattern or 3D texture.
Should not have
• The basic picture/design I uploaded is just a suggestion, but there isn't really anything there.

```html
<!DOCTYPE html>
<html lang="en">
<head>
<meta charset="utf-8">
<title>The Thornwell Law Group</title>
<link rel="stylesheet" href="https://fonts.googleapis.com/css2?family=Source+Sans+3:wght@400;600;700&family=Roboto+Condensed:ital,wght@1,300&display=swap">
<style>
  :root {
    --blue: #0a90d0;
    --blue-text: #0692cd;
    --orange: #f78f20;
    --orange-soft: #faa54b;
    --brown: #6a3905;
    --field: #f2e9ea;
    --ink: #2b2b2b;
    --footer: #05679a;
    --white: #ffffff;
  }
  * { margin: 0; padding: 0; box-sizing: border-box; }
  html, body { width: 1200px; height: 1132px; overflow: hidden; background: var(--white); }
  body { font-family: "Source Sans 3", sans-serif; color: var(--ink); }
  .page { position: relative; width: 1200px; height: 1132px; overflow: hidden; }
  .backdrop { position: absolute; left: 0; top: 0; }
  .portrait {
    position: absolute; left: 24px; top: 130px; width: 418px; height: 644px;
    background: linear-gradient(180deg, #6e6e6e 0%, #2e2e2e 45%, #1c1c1c 100%);
    border-radius: 180px 180px 0 0;
  }
  .brand {
    position: absolute; left: 70px; top: 42px;
    font-size: 34px; font-weight: 700; color: var(--white); letter-spacing: 0.2px;
  }
  .phone {
    position: absolute; left: 893px; top: 42px;
    display: flex; align-items: center; gap: 12px;
    font-family: "Roboto Condensed", sans-serif; font-style: italic; font-weight: 300;
    font-size: 40px; color: var(--blue-text);
  }
  .phone svg { display: block; }
  .values { position: absolute; left: 727px; top: 164px; width: 410px; }
  .value { position: absolute; left: 0; width: 410px; }
  .value h2 { font-size: 21px; font-weight: 700; color: var(--blue-text); line-height: 1.2; }
  .value p { margin-top: 3px; font-size: 16.5px; line-height: 22px; color: var(--ink); }
  .value--fees { top: 0; }
  .value--easy { top: 90px; }
  .value--firm { top: 188px; left: 2px; }
  .tagline { position: absolute; left: 41px; top: 798px; color: var(--white); }
  .tagline .lead { font-size: 34px; font-weight: 600; line-height: 1; }
  .tagline .main { margin-top: 2px; font-size: 92px; font-weight: 700; line-height: 1; letter-spacing: 0.5px; }
  .question-box {
    position: absolute; left: 734px; top: 511px; width: 396px; height: 541px;
    background: var(--orange);
  }
  .question-box h3 {
    position: absolute; left: 40px; top: 32px;
    font-size: 28px; font-weight: 700; color: var(--white);
  }
  .field {
    position: absolute; left: 41px; width: 316px; height: 49px;
    background: var(--field); padding: 12px 17px;
    font-size: 16px; color: #666;
  }
  .field--name { top: 90px; }
  .field--phone { top: 151px; }
  .field--email { top: 213px; }
  .field--message { top: 276px; height: 170px; }
  .ask-button {
    position: absolute; left: 44px; top: 460px; width: 139px; height: 52px;
    background: var(--brown); border-radius: 3px;
    color: var(--white); font-size: 28px; font-weight: 700; letter-spacing: 1px;
    display: flex; align-items: center; justify-content: center;
  }
  .footer {
    position: absolute; left: 0; top: 1084px; width: 1200px; height: 48px;
    background: var(--footer); color: #d4e6f1;
    font-size: 15px; display: flex; align-items: center; justify-content: center;
    padding-left: 62px;
  }
</style>
</head>
<body>
<div class="page">
  <svg class="backdrop" width="1200" height="1132" viewBox="0 0 1000 943" preserveAspectRatio="none" aria-hidden="true">
    <path d="M594 12 C567 150 563 300 576 450 L577 600 L552 690 L540 690 L560 450 C550 300 556 150 586 12 Z" fill="#faa54b"/>
    <path d="M0 0 L585 0 C560 150 555 300 567 450 L568 558 L598 557 L492 803 L0 780 Z" fill="#0a90d0"/>
  </svg>

  <div class="portrait" role="img" aria-label="Portrait photo of the attorney in a dark suit and striped tie"></div>

  <div class="brand">THORNWELL LAW GROUP</div>

  <div class="phone">
    <svg width="12" height="22" viewBox="0 0 12 22" aria-hidden="true">
      <rect x="1" y="3" width="10" height="18" rx="1.5" fill="#2b2b2b"/>
      <rect x="3" y="5" width="6" height="6" fill="#ffffff"/>
      <rect x="8" y="0" width="2" height="4" fill="#2b2b2b"/>
    </svg>
    <span>504-917-2083</span>
  </div>

  <div class="values">
    <div class="value value--fees">
      <h2>Never More Than 24%</h2>
      <p>We charge less than other firms, so you keep more.</p>
    </div>
    <div class="value value--easy">
      <h2>We Make It Easy</h2>
      <p>Modern technology keeps your whole case simple, easy and hassle-free.</p>
    </div>
    <div class="value value--firm">
      <h2>Big Firm Lawyering</h2>
      <p>Experience trying and settling multi-million dollar cases, with success.</p>
    </div>
  </div>

  <div class="tagline">
    <div class="lead">Car Wreck? Know Your Lawyer.</div>
    <div class="main">We Can Help.</div>
  </div>

  <div class="question-box">
    <h3>Quick Question ?</h3>
    <div class="field field--name">Name</div>
    <div class="field field--phone">Phone</div>
    <div class="field field--email">Email</div>
    <div class="field field--message">Your Message</div>
    <div class="ask-button">ASK</div>
  </div>

  <div class="footer">Copyright © 2016 Thornwell Law.&nbsp; Agreement and Privacy Policy.</div>
</div>
</body>
</html>
```